2 x storefront vinyl request

We are transitioning to a storefront office and need two vinyls for the windows.

First vinyl: Use the Dalton Rivers logo, website (www.daltonriversholdings.example) and leasing office number ((555) 318-4472)

Second vinyl: Maintenance Division & phone number (555) 318-4472

```html
<!DOCTYPE html>
<html lang="en">
<head>
<meta charset="utf-8">
<title>Dalton Rivers Properties – Storefront Vinyls</title>
<link rel="stylesheet" href="https://fonts.googleapis.com/css2?family=Bebas+Neue&family=Montserrat:wght@800&family=Roboto+Condensed:wght@600;700&display=swap">
<style>
  :root {
    --backdrop: #5a5a5a;
    --vinyl-white: #ffffff;
    --vinyl-black: #000000;
    --ink: #1c1c1c;
  }
  * { margin: 0; padding: 0; box-sizing: border-box; }
  html, body {
    width: 1200px; height: 717px; overflow: hidden;
    background: var(--backdrop);
  }
  .canvas {
    position: relative; width: 1200px; height: 717px;
    display: flex; justify-content: center; align-items: center; gap: 80px;
  }
  .vinyl {
    position: relative; width: 290px; height: 580px;
    background: var(--vinyl-white);
    box-shadow: 0 6px 18px rgba(0,0,0,0.35);
    overflow: hidden;
  }
  .vinyl__band {
    position: absolute; inset: 0; width: 100%; height: 100%;
  }
  .brand {
    position: absolute; top: 86px; left: 0; right: 0;
    display: flex; justify-content: center; align-items: center; gap: 10px;
  }
  .brand__mark {
    width: 14px; height: 14px; background: var(--ink);
  }
  .brand__name {
    font-family: "Roboto Condensed", sans-serif; font-weight: 700;
    font-size: 16px; line-height: 17px; color: var(--ink);
    text-transform: uppercase; letter-spacing: 0.3px;
  }
  .vinyl__title {
    position: absolute; top: 268px; left: 0; right: 0;
    text-align: center; color: var(--vinyl-white);
    font-family: "Bebas Neue", sans-serif; font-size: 50px; line-height: 47px;
    letter-spacing: 0.5px;
  }
  .vinyl__phone {
    position: absolute; top: 392px; left: 28px; width: 234px; height: 36px;
    background: var(--vinyl-white); border-radius: 18px;
    display: flex; align-items: center; justify-content: center;
    font-family: "Montserrat", sans-serif; font-weight: 800; font-size: 22px;
    color: var(--vinyl-black);
  }
  .vinyl__web {
    position: absolute; top: 510px; left: 0; right: 0; text-align: center;
    font-family: "Roboto Condensed", sans-serif; font-weight: 700; font-size: 12px;
    letter-spacing: 1px; color: var(--vinyl-black);
  }
</style>
</head>
<body>
<main class="canvas">
  <article class="vinyl vinyl--leasing">
    <svg class="vinyl__band" viewBox="0 0 555 1110" preserveAspectRatio="none" aria-hidden="true">
      <polygon points="0,505 555,403 555,841 0,943" fill="var(--vinyl-black)"/>
    </svg>
    <div class="brand">
      <span class="brand__mark"></span>
      <span class="brand__name">Dalton Rivers<br>Properties</span>
    </div>
    <h1 class="vinyl__title">Leasing<br>Office</h1>
    <p class="vinyl__phone">(555) 318-4472</p>
    <p class="vinyl__web">DaltonRiversHoldings.example</p>
  </article>

  <article class="vinyl vinyl--maintenance">
    <svg class="vinyl__band" viewBox="0 0 555 1110" preserveAspectRatio="none" aria-hidden="true">
      <polygon points="0,505 555,403 555,841 0,943" fill="var(--vinyl-black)"/>
    </svg>
    <div class="brand">
      <span class="brand__mark"></span>
      <span class="brand__name">Dalton Rivers<br>Properties</span>
    </div>
    <h1 class="vinyl__title">Maintenance<br>Division</h1>
    <p class="vinyl__phone">(555) 318-4472</p>
    <p class="vinyl__web">DaltonRiversHoldings.example</p>
  </article>
</main>
</body>
</html>
```